Marvia Quenby Business Cards

We Need two Business Cards with bleeds. the only difference between the two cards is the backaround color one lilac and pink. Attached we have the cards please match up the logo's and text. Take out the orange box out.

Target Market(s)

double-sided business cards

Industry/Entity Type

Business

Logo Text

match up as best as possible

Colors
f59195
d2a4cc

Requirements
Must have
• n/a
Nice to have
• n/a
Should not have
• n/a

```html
<!DOCTYPE html>
<html lang="en">
<head>
<meta charset="utf-8">
<title>Marvia Quenby Business Cards</title>
<link href="https://fonts.googleapis.com/css2?family=Questrial&display=swap" rel="stylesheet">
<style>
  :root {
    --page: #eef0f1;
    --pink: #f59195;
    --lilac: #d2a4cc;
    --frame: #c4165a;
    --ink: #111111;
    --accent: #c4165a;
    --on-dark: #f7eef2;
    --poly-dark: #5c1f4a;
    --poly-mid: #8a2452;
    --poly-light: #a8314f;
    --badge: #d4ad3c;
  }
  * { box-sizing: border-box; margin: 0; padding: 0; }
  html, body { width: 1200px; height: 800px; overflow: hidden; }
  body {
    background: var(--page);
    font-family: "Questrial", "Century Gothic", sans-serif;
    color: var(--ink);
    position: relative;
  }
  .card {
    position: absolute;
    top: 240px;
    width: 560px;
    height: 320px;
    border: 8px solid var(--frame);
    overflow: hidden;
  }
  .card--pink { left: 25px; background: var(--pink); }
  .card--lilac { left: 615px; background: var(--lilac); }
  .card__art { position: absolute; left: 0; top: 0; width: 544px; height: 304px; }
  .card__name {
    position: absolute; right: 22px; top: 26px;
    font-size: 29px; font-weight: 400; color: var(--accent); white-space: nowrap;
  }
  .card__cert {
    position: absolute; left: 290px; top: 66px;
    font-size: 13px;
  }
  .card__title {
    position: absolute; right: 16px; top: 92px;
    font-size: 22px; white-space: nowrap;
  }
  .card__appt {
    position: absolute; right: 16px; top: 122px;
    font-size: 10px;
  }
  .card__contacts {
    position: absolute; left: 250px; top: 164px;
    list-style: none; font-size: 14px;
  }
  .card__contacts li { display: flex; align-items: center; gap: 8px; height: 26px; white-space: nowrap; }
  .card__contacts svg { width: 18px; height: 18px; flex: none; }
  .card__brand {
    position: absolute; left: 20px; top: 160px;
    display: flex; align-items: center; gap: 8px;
    font-size: 11px; color: var(--on-dark); white-space: nowrap;
  }
  .card__brand-dot {
    width: 32px; height: 32px; border-radius: 50%;
    background: var(--badge); flex: none;
  }
</style>
</head>
<body>

<section class="card card--pink">
  <svg class="card__art" viewBox="0 0 544 304" role="img" aria-label="Low-poly geometric pattern in plum and wine tones">
    <defs>
      <linearGradient id="polyA" x1="0" y1="0" x2="1" y2="1">
        <stop offset="0" stop-color="#5c1f4a"/>
        <stop offset="1" stop-color="#8a2452"/>
      </linearGradient>
      <linearGradient id="polyB" x1="0" y1="0" x2="1" y2="1">
        <stop offset="0" stop-color="#8a2452"/>
        <stop offset="1" stop-color="#a8314f"/>
      </linearGradient>
    </defs>
    <polygon points="0,100 180,140 130,250 0,220" fill="url(#polyA)"/>
    <polygon points="120,304 200,235 300,304" fill="url(#polyB)"/>
  </svg>
  <h1 class="card__name">Marvia Quenby-Ashcombe MD</h1>
  <p class="card__cert">Board Certified</p>
  <p class="card__title">Women's Health &amp; Wellness Specialist</p>
  <p class="card__appt">By Appointment</p>
  <ul class="card__contacts">
    <li><svg viewBox="0 0 24 24"><path d="M12 2a7 7 0 0 0-7 7c0 5 7 13 7 13s7-8 7-13a7 7 0 0 0-7-7z" fill="none" stroke="#111" stroke-width="2"/><circle cx="12" cy="9" r="2.5" fill="#111"/></svg>418 Alder Road, Fairhaven NY 11290</li>
    <li><svg viewBox="0 0 24 24"><circle cx="12" cy="12" r="10" fill="none" stroke="#111" stroke-width="2"/><path d="M8 7l2 0 1 3-1.5 1a6 6 0 0 0 3.5 3.5l1-1.5 3 1 0 2c-5 1-10-4-9-9z" fill="#111"/></svg>555 310 4821/4822</li>
    <li><svg viewBox="0 0 24 24"><path d="M3 9l9-6 9 6v11H3z M3 9l9 6 9-6" fill="none" stroke="#111" stroke-width="2"/></svg>m-quenby@brightmail.net</li>
  </ul>
  <div class="card__brand"><span class="card__brand-dot"></span><span>Quenby Wellness</span></div>
</section>

<section class="card card--lilac">
  <svg class="card__art" viewBox="0 0 544 304" role="img" aria-label="Low-poly geometric pattern in plum and wine tones">
    <polygon points="0,100 180,140 130,250 0,220" fill="url(#polyA)"/>
    <polygon points="120,304 200,235 300,304" fill="url(#polyB)"/>
  </svg>
  <h1 class="card__name">Marvia Quenby-Ashcombe MD</h1>
  <p class="card__cert">Board Certified</p>
  <p class="card__title">Women's Health &amp; Wellness Specialist</p>
  <p class="card__appt">By Appointment</p>
  <ul class="card__contacts">
    <li><svg viewBox="0 0 24 24"><path d="M12 2a7 7 0 0 0-7 7c0 5 7 13 7 13s7-8 7-13a7 7 0 0 0-7-7z" fill="none" stroke="#111" stroke-width="2"/><circle cx="12" cy="9" r="2.5" fill="#111"/></svg>418 Alder Road, Fairhaven NY 11290</li>
    <li><svg viewBox="0 0 24 24"><circle cx="12" cy="12" r="10" fill="none" stroke="#111" stroke-width="2"/><path d="M8 7l2 0 1 3-1.5 1a6 6 0 0 0 3.5 3.5l1-1.5 3 1 0 2c-5 1-10-4-9-9z" fill="#111"/></svg>555 310 4821/4822</li>
    <li><svg viewBox="0 0 24 24"><path d="M3 9l9-6 9 6v11H3z M3 9l9 6 9-6" fill="none" stroke="#111" stroke-width="2"/></svg>m-quenby@brightmail.net</li>
  </ul>
  <div class="card__brand"><span class="card__brand-dot"></span><span>Quenby Wellness</span></div>
</section>

</body>
</html>
```